Bicycle Tour Schedule on a Business Card

Need to develop a 2 side business card that highlights a series of bike tours on 1 side and a series of events on the other side.
This will be inserted into a card wallet that attaches to a cell phone and will be handed out at an expo. The card wallets are black and red so color must coordinate with both. There is a photo of the card wallets attached.

1 side needs to be devoted to Pedal Vista Rides and the others to KRV Outcome events on the other. Dates and websites are very important.

Target Market(s)

Cyclists
Predominantly men ages 40+
Educated, Professionals

Industry/Entity Type

Business

Font styles to use
Serif

Requirements
Must have
• Pedal vista rides logo on 1 side and KRV Outcome logo on the other side
• dates and websites clearly visible
• Design of both sides must go together.
• Must be portrait not landscape

```html
<!DOCTYPE html>
<html lang="en">
<head>
<meta charset="utf-8">
<title>Pedal Vista Rides &amp; KRV Outcome – Event Cards</title>
<link rel="stylesheet" href="https://fonts.googleapis.com/css2?family=Open+Sans:wght@400;700&display=swap">
<style>
  :root {
    --page-bg: #e6e6e6;
    --card-white: #ffffff;
    --card-black: #0b0b0b;
    --brand-red: #e8202a;
    --ink-white: #ffffff;
    --ink-black: #0b0b0b;
  }
  html, body {
    margin: 0;
    width: 1200px;
    height: 982px;
    overflow: hidden;
    background: var(--page-bg);
    font-family: "Open Sans", Arial, sans-serif;
  }
  .card-pair {
    position: absolute;
    inset: 0;
    display: flex;
    justify-content: center;
    align-items: center;
    gap: 60px;
  }
  .card {
    display: block;
    width: 420px;
    height: 735px;
    box-shadow: 0 6px 18px rgba(0,0,0,0.18);
  }
  .card-face-white { fill: var(--card-white); }
  .card-face-black { fill: var(--card-black); }
  .band-red { fill: var(--brand-red); }
  .band-black { fill: var(--card-black); }
  .divider-white { fill: var(--ink-white); }
  .divider-black { fill: var(--card-black); }
  .band-title {
    font-family: "Open Sans", Arial, sans-serif;
    font-weight: 700;
    font-size: 26px;
    fill: var(--ink-white);
    text-anchor: middle;
    letter-spacing: 0.5px;
  }
  .band-title-lead { font-size: 28px; }
  .band-title-tour { font-size: 24px; }
  .band-detail {
    font-family: "Open Sans", Arial, sans-serif;
    font-weight: 400;
    font-size: 14px;
    fill: var(--ink-white);
    text-anchor: middle;
    letter-spacing: 0.4px;
  }
  .band-detail-small { font-size: 12px; }
  .brand-name {
    font-family: "Open Sans", Arial, sans-serif;
    font-weight: 700;
    fill: var(--brand-red);
  }
  .brand-mark { fill: var(--brand-red); }
</style>
</head>
<body>
<main class="card-pair">

  <!-- Events side -->
  <svg class="card card-events" viewBox="0 0 420 735" width="420" height="735" aria-label="KRV Outcome events card">
    <rect class="card-face-white" width="420" height="735"/>

    <g class="brand-lockup">
      <rect class="brand-mark" x="26" y="52" width="22" height="22"/>
      <text class="brand-name" x="58" y="71" font-size="20">KRV OUTCOME</text>
    </g>

    <g class="event-bands" transform="translate(210 440) rotate(-28)">
      <rect class="band-red" x="-700" y="-252" width="1400" height="254"/>
      <rect class="divider-white" x="-700" y="-189" width="1400" height="3"/>
      <rect class="divider-white" x="-700" y="-125" width="1400" height="3"/>
      <rect class="divider-white" x="-700" y="-61" width="1400" height="3"/>

      <rect class="band-black" x="-700" y="12" width="1400" height="64"/>
      <rect class="band-black" x="-700" y="82" width="1400" height="64"/>
      <rect class="band-black" x="-700" y="152" width="1400" height="64"/>

      <text class="band-title band-title-lead" x="112" y="-210">TRIO WHEEL SERIES:</text>

      <text class="band-title" x="83" y="-153">CYCLING CAMPS FOR YOUTH</text>
      <text class="band-detail" x="83" y="-134">TRIOWHEELSERIES.ORG</text>

      <text class="band-title" x="47" y="-89">MOUNTAIN BIKE CAMP</text>
      <text class="band-detail" x="47" y="-70">JULY 8-10, 2016</text>

      <text class="band-title" x="14" y="-25">CYCLOCROSS CAMP</text>
      <text class="band-detail" x="14" y="-6">AUG 26-28, 2016</text>

      <text class="band-title" x="-24" y="44">SUMMIT CENTURY RIDE</text>
      <text class="band-detail" x="-24" y="64">JUNE 18, 2016 SUMMITCENTURYRIDE.COM</text>

      <text class="band-title" x="-60" y="114">TRAIL 2 TRAIL CHALLENGE</text>
      <text class="band-detail" x="-60" y="134">JULY 30, 2016  TRAIL2TRAIL.COM</text>

      <text class="band-title" x="-73" y="184">ZANY WHEEL RIDE</text>
      <text class="band-detail" x="-73" y="204">SEPTEMBER 11, 2016 ZANYWHEELRIDE.COM</text>
    </g>
  </svg>

  <!-- Tours side -->
  <svg class="card card-tours" viewBox="0 0 420 735" width="420" height="735" aria-label="Pedal Vista Rides tours card">
    <rect class="card-face-black" width="420" height="735"/>

    <g class="brand-lockup">
      <circle class="brand-mark" cx="150" cy="78" r="12"/>
      <text class="brand-name" x="172" y="72" font-size="22">PEDAL VISTA</text>
      <text class="brand-name" x="172" y="96" font-size="22">RIDES</text>
    </g>

    <g class="tour-bands" transform="translate(210 440) rotate(-28)">
      <rect class="band-red" x="-700" y="-200" width="1400" height="70"/>
      <rect class="band-red" x="-700" y="-122" width="1400" height="64"/>
      <rect class="band-red" x="-700" y="-50" width="1400" height="64"/>
      <rect class="band-red" x="-700" y="22" width="1400" height="64"/>
      <rect class="band-red" x="-700" y="94" width="1400" height="64"/>

      <text class="band-title band-title-tour" x="92" y="-168">FULLY SUPPORTED BIKE TOURS</text>
      <text class="band-detail band-detail-small" x="92" y="-148">DISCOVER THE HIDDEN GEMS ON TWO WHEELS</text>

      <text class="band-title" x="48" y="-89">HEART OF COLORADO</text>
      <text class="band-detail" x="48" y="-69">JUNE 26 - JULY 2, 2016</text>

      <text class="band-title" x="9" y="-17">CO FRONT RANGE TOUR</text>
      <text class="band-detail" x="9" y="3">AUGUST 14-20, 2016</text>

      <text class="band-title" x="-28" y="55">CAPE COD TOUR</text>
      <text class="band-detail" x="-28" y="75">OCTOBER 9-15, 2016</text>

      <text class="band-title" x="-67" y="127">FLORIDA KEYS TOUR</text>
      <text class="band-detail band-detail-small" x="-67" y="147">NOVEMBER 6-12 &amp; DECEMBER 4-10, 2016</text>
    </g>
  </svg>

</main>
</body>
</html>
```